Conference flyer

We need a flyer for a conference for the defence industry. The attached has been updated with new information using last years flyer. We would like something new and fresh. Please note the theme of the conference is 'a global environment'.

The final design should reflect the defence industry and manufacturing.

Defence

```html
<!DOCTYPE html>
<html lang="en">
<head>
<meta charset="utf-8">
<title>Defence Trade Controls Annual Conference Flyer</title>
<link rel="stylesheet" href="https://fonts.googleapis.com/css2?family=Arimo:wght@400;700&family=Roboto+Slab:wght@700&family=Tinos&display=swap">
<style>
:root{
  --board:#ffffff;
  --paper:#ffffff;
  --ink:#2f2f2f;
  --muted:#6b6b6b;
  --blue:#4a9ad6;
  --cover-blue:#5ba7de;
  --rule:#a9cdea;
  --grey-box:#e2e2e2;
  --photo:#c9c9c9;
}
*{box-sizing:border-box;margin:0;padding:0}
html,body{width:1200px;height:1000px;overflow:hidden;background:var(--board)}
body{position:relative;font-family:"Arimo",Arial,sans-serif;color:var(--ink)}
.board-title{position:absolute;top:26px;left:0;width:1200px;text-align:center;font-family:"Tinos","Times New Roman",serif;font-size:24px;font-weight:400;color:#111}
.page{position:absolute;width:300px;height:425px;background:var(--paper);box-shadow:3px 4px 6px rgba(0,0,0,.35);overflow:hidden}
.p1{left:100px;top:75px}.p2{left:450px;top:75px}.p3{left:800px;top:75px}
.p4{left:100px;top:528px}.p5{left:450px;top:528px}.p6{left:800px;top:528px}
.flags{background:linear-gradient(100deg,#c8102e 0 12%,#f2f2f2 12% 20%,#2a4e9c 20% 34%,#3a9a43 34% 48%,#ffd200 48% 58%,#e8e8e8 58% 66%,#1f4fa0 66% 100%);}
.band{position:absolute;left:15px;top:15px;width:270px;height:45px}
.heading{position:absolute;left:15px;color:var(--blue);font-size:9.5px;font-weight:400}
.folio{position:absolute;bottom:12px;font-size:4px;color:var(--muted)}
.folio.l{left:15px}.folio.r{right:15px}
/* cover */
.cover-panel{position:absolute;left:15px;top:15px;width:270px;height:173px;background:var(--cover-blue);color:#fff;padding:47px 14px 0}
.cover-title{font-family:"Roboto Slab",serif;font-size:15px;line-height:17px;font-weight:700}
.cover-sub{font-size:7px;margin-top:5px;opacity:.95}
.cover-pres{font-size:5.6px;font-weight:700;margin-top:12px;line-height:7.5px}
.cover-meta{font-size:5.3px;margin-top:3px;line-height:9px}
.cover-photo{position:absolute;left:15px;top:188px;width:270px;height:188px}
.sponsors{position:absolute;left:15px;top:390px;width:270px;display:flex;align-items:center;gap:16px;font-size:5px;color:var(--muted)}
.sponsor{display:flex;align-items:center;gap:3px;font-weight:700;color:#555;font-size:5.5px}
.sponsor i{width:10px;height:10px;border-radius:50%;background:#8a9a7a;display:block}
/* speakers */
.speakers{position:absolute;left:15px;top:104px;width:270px;display:grid;grid-template-columns:repeat(3,70px);column-gap:22px;row-gap:10px}
.speaker .photo{width:70px;height:57px;background:var(--photo)}
.speaker .photo.empty{background:var(--grey-box)}
.speaker h3{color:var(--blue);font-size:5.5px;margin-top:5px}
.speaker p{font-size:4.2px;line-height:5.2px;color:var(--ink)}
.more{position:absolute;left:200px;top:381px;font-size:4.2px}
/* agenda */
.agenda{position:absolute;left:15px;top:104px;width:270px;display:grid;grid-template-columns:1fr 1fr;column-gap:12px}
.day{font-size:6.5px;margin-bottom:7px}.day b{font-weight:700}
.slot{display:flex;font-size:4.2px;line-height:5.2px;margin-bottom:7px}
.slot .t{width:34px;flex:none;white-space:nowrap}
.slot .e{font-weight:700}
.slot ul{font-weight:400;list-style:none;margin-top:1px;padding-left:3px}
.slot li{margin-bottom:1.5px}
.slot li:before{content:"○ ";font-size:3.5px}
/* training & prices */
.sub{position:absolute;left:15px;font-size:6.5px;font-weight:700}
.rowline{position:absolute;left:15px;width:270px;border-top:.6px solid var(--rule);border-bottom:.6px solid var(--rule);font-size:4.2px;display:flex;padding:4px 0}
.rowline .d{width:52px;flex:none}
.prices{position:absolute;left:15px;top:245px;width:270px;border-collapse:collapse;font-size:4.4px}
.prices th{font-weight:700;text-align:center;padding:4px 0;vertical-align:bottom}
.prices td{text-align:center;padding:8px 0;border-top:.6px solid var(--rule)}
.prices td:first-child,.prices th:first-child{text-align:left;font-weight:700}
/* info */
.info{position:absolute;left:15px;top:102px;width:270px;border-collapse:collapse;font-size:4.1px;line-height:5px}
.info th{text-align:left;width:70px;font-weight:700;vertical-align:top;padding:3.5px 0;border-top:.6px solid var(--rule)}
.info td{vertical-align:top;padding:3.5px 0;border-top:.6px solid var(--rule)}
.info a{color:var(--blue);text-decoration:none}
.contact{position:absolute;left:15px;top:363px;width:270px;display:flex;gap:22px;font-size:4.2px}
.contact div{display:flex;gap:5px;align-items:flex-start}
.contact b{display:block}
.howto{position:absolute;left:15px;top:352px;font-size:4.3px}
/* registration */
.form{position:absolute;left:15px;top:100px;width:130px;font-size:4.2px}
.field{border-bottom:.6px solid var(--rule);padding:3px 0 2px}
.form h4,.modules h4{font-size:4.6px;font-weight:700;margin:10px 0 4px}
.check{display:flex;align-items:center;gap:3px;margin-bottom:4px}
.box{width:5px;height:5px;border:.6px solid var(--blue);display:inline-block;flex:none}
.cards{display:flex;gap:8px;margin-bottom:3px}
.note{font-size:3.4px;color:var(--muted);margin-top:3px}
.modules{position:absolute;left:155px;top:100px;width:130px;font-size:4.2px;line-height:5.2px}
.modules h4:first-child{margin-top:0}
.mod{margin-bottom:4px}
.mod .desc{display:block;padding-left:8px}
.att{margin-top:4px}
.att .row{display:flex;gap:3px;align-items:center}
.office{position:absolute;left:15px;top:335px;width:270px;height:72px;background:var(--grey-box);padding:10px 10px;font-size:4.2px}
.office b{display:block;margin-bottom:3px}
.office div{border-bottom:.6px solid #999;padding:2px 0;width:250px}
</style>
</head>
<body>
<h1 class="board-title">Defence Trade Controls Annual Flyer Design_01</h1>

<section class="page p1">
  <div class="cover-panel">
    <div class="cover-title">Defence Trade Controls<br>Annual Conference</div>
    <div class="cover-sub">Trade Controls in a Global Environment</div>
    <div class="cover-pres">Presenting the DTC 2015 Conference<br>Australia's Annual Defence Industry Global Trade Controls Conference</div>
    <div class="cover-meta">Tuesday, 2 June 2015 and Wednesday, 3 June 2015<br>Regent Harbour Melbourne</div>
  </div>
  <div class="cover-photo flags" role="img" aria-label="Keyboard keys printed with national flags of many countries"></div>
  <div class="sponsors">
    <span>Sponsored By:</span>
    <span class="sponsor"><i></i>Corvane</span>
    <span class="sponsor">Keystone Industry</span>
    <span class="sponsor">MERIDIAN</span>
    <span class="sponsor"><i></i>Tradewise</span>
  </div>
</section>

<section class="page p2">
  <div class="band flags" role="img" aria-label="Flag keyboard keys banner"></div>
  <h2 class="heading" style="top:80px">Featuring Presentations From:</h2>
  <div class="speakers">
    <div class="speaker"><div class="photo empty" role="img" aria-label="Speaker portrait placeholder"></div><h3>Helena Marsh</h3><p>Assistant Secretary<br>Defence Export Licensing Office</p></div>
    <div class="speaker"><div class="photo" role="img" aria-label="Portrait of Victor Dimas"></div><h3>Victor Dimas</h3><p>Import/Export Compliance Manager<br>Arcwell Systems Australia</p></div>
    <div class="speaker"><div class="photo" role="img" aria-label="Portrait of Owen Calder"></div><h3>Owen Calder</h3><p>Calder Brooks PLLC</p></div>
    <div class="speaker"><div class="photo" role="img" aria-label="Portrait of Renata Voss"></div><h3>Renata Voss</h3><p>Managing Director<br>Voss Trade Advisors LLC</p></div>
    <div class="speaker"><div class="photo" role="img" aria-label="Portrait of Lin Tao"></div><h3>Lin Tao</h3><p>Global Trade Compliance Director<br>Semiconductors</p></div>
    <div class="speaker"><div class="photo" role="img" aria-label="Portrait of Carol-Ann Whitby"></div><h3>Carol-Ann Whitby</h3><p>Director<br>Global Trade Management<br>Halvern Aerospace Corporation</p></div>
    <div class="speaker"><div class="photo" role="img" aria-label="Portrait of Graham Pellow"></div><h3>Graham Pellow</h3><p>Director Compliance<br>Commercial and Policy<br>Allied Materiel Sales Office</p></div>
    <div class="speaker"><div class="photo" role="img" aria-label="Portrait of Neil Carver"></div><h3>Neil Carver</h3><p>Partner<br>International Trade<br>Global Compliance Partners</p></div>
    <div class="speaker"><div class="photo empty" role="img" aria-label="Speaker portrait placeholder"></div><h3>Sean Delaney</h3><p>Director<br>Harbourline Freight Ltd</p></div>
  </div>
  <div class="more">...plus many more</div>
  <div class="folio l">2 &nbsp; Defence Trade Controls Annual Conference</div>
</section>

<section class="page p3">
  <div class="band flags" role="img" aria-label="Flag keyboard keys banner"></div>
  <h2 class="heading" style="top:83px">Agenda</h2>
  <div class="agenda">
    <div>
      <div class="day"><b>Day 1:</b> Tuesday, 2 June 2015</div>
      <div class="slot"><span class="t">0830 – 0900</span><span class="e">Registration</span></div>
      <div class="slot"><span class="t">0900 – 0915</span><span class="e">Chair's Welcome and<br>Opening Address</span></div>
      <div class="slot"><span class="t">0915 – 0950</span><span class="e">Australian Legislative Changes</span></div>
      <div class="slot"><span class="t">0950 – 1030</span><span class="e">Export Control Reform – Next Steps</span></div>
      <div class="slot"><span class="t">1030 – 1100</span><span class="e">Morning Tea and Networking</span></div>
      <div class="slot"><span class="t">1100 – 1145</span><span class="e">Managing Multi-jurisdictional<br>Programs</span></div>
      <div class="slot"><span class="t">1145 – 1230</span><span class="e">Country Focus: Japan</span></div>
      <div class="slot"><span class="t">1230 – 1330</span><span class="e">Lunch</span></div>
      <div class="slot"><span class="t">1330 – 1400</span><span class="e">Export Control Reform and<br>FMS, CoA Management</span></div>
      <div class="slot"><span class="t">1400 – 1430</span><span class="e">Country Focus: Singapore</span></div>
      <div class="slot"><span class="t">1430 – 1500</span><span class="e">Customs Trusted Trader Program</span></div>
      <div class="slot"><span class="t">1500 – 1530</span><span class="e">Afternoon Tea and Networking</span></div>
      <div class="slot"><span class="t">1530 – 1645</span><span class="e">Industry Best Practice<br><span style="font-weight:400;font-style:italic">Panel Led by Neil Carver</span></span></div>
      <div class="slot"><span class="t">1645 – 1730</span><span class="e">Day One Wrap Up</span></div>
      <div class="slot"><span class="t">1730</span><span class="e">Reception</span></div>
    </div>
    <div>
      <div class="day"><b>Day 2:</b> Wednesday, 3 June 2015</div>
      <div class="slot"><span class="t">0900 – 0910</span><span class="e">Chair's Welcome Back</span></div>
      <div class="slot"><span class="t">0910 – 0930</span><span class="e">Best Practice Compliance</span></div>
      <div class="slot"><span class="t">0930 – 1030</span><span class="e">Compliance Case Study</span></div>
      <div class="slot"><span class="t">1030 – 1100</span><span class="e">Morning Tea and Networking</span></div>
      <div class="slot"><span class="t">1100 – 1130</span><span class="e">Practical Management of<br>Export Control Reform</span></div>
      <div class="slot"><span class="t">1130 – 1200</span><span class="e">EAR Exceptions – The Good,<br>The Bad and The Ugly</span></div>
      <div class="slot"><span class="t">1200 – 1245</span><span class="e">Country Focus: European Union</span></div>
      <div class="slot"><span class="t">1245 – 1345</span><span class="e">Lunch and Networking</span></div>
      <div class="slot"><span class="t">1345 – 1500</span><span class="e">Export Control –<br>Round Table Discussions
        <ul><li>Dual National Exemptions</li><li>Understanding 'Specially Designed'<br>&nbsp;&nbsp;Definitions</li><li>Re-exports Under EAR</li><li>US Trade Co-operation Treaty</li><li>Securing Your Supply Chain</li></ul></span></div>
      <div class="slot"><span class="t">1500 – 1530</span><span class="e">Conference Q&amp;A and Wrap Up</span></div>
      <div class="slot"><span class="t">1530</span><span class="e">Conference Close</span></div>
    </div>
  </div>
  <div class="folio r">Defence Trade Controls Annual Conference &nbsp; 3</div>
</section>

<section class="page p4">
  <div class="band flags" role="img" aria-label="Flag keyboard keys banner"></div>
  <h2 class="heading" style="top:83px">4 x Half Day Pre and Post Training Sessions</h2>
  <div class="sub" style="top:102px">Pre Conference Training Modules</div>
  <div class="rowline" style="top:115px"><span class="d">Monday, 1 June 2015</span><span><b>Module 1:</b> Export Controls for Beginners – Helping Beginners to Make the Best of<br>the Conference</span></div>
  <div class="sub" style="top:154px">Post Conference Training Modules</div>
  <div class="rowline" style="top:167px"><span class="d">Thursday, 4 June 2015</span><span><b>Module 2:</b> Practical Management of Export Control Reform<br><b>Module 3:</b> Tips and Hints for Best Practice Compliance</span></div>
  <div class="rowline" style="top:186px;border-top:none"><span class="d">Friday, 5 June 2015</span><span><b>Module 4:</b> Making the Best of Commerce Exceptions</span></div>
  <h2 class="heading" style="top:224px">Conferences Prices (All prices include GST)</h2>
  <table class="prices">
    <tr><th></th><th>Super Earlybird<br>(Prior 31 December 2014)</th><th>Earlybird<br>(Prior 31 March 2015)</th><th>Standard Pricing</th></tr>
    <tr><td>Conference Only</td><td>$1,095</td><td>$1,195</td><td>$1,295</td></tr>
    <tr><td>Training Module (ea)<br>(With Conference)</td><td>$350</td><td>$399</td><td>$450</td></tr>
    <tr><td>Training Module (ea) Only</td><td>$399</td><td>$450</td><td>$495</td></tr>
  </table>
  <div class="folio l">4 &nbsp; Defence Trade Controls Annual Conference</div>
</section>

<section class="page p5">
  <div class="band flags" role="img" aria-label="Flag keyboard keys banner"></div>
  <h2 class="heading" style="top:83px">General Information</h2>
  <table class="info">
    <tr><th>Conference Venue:</th><td>Regent Harbour Melbourne<br>14 Quayside Rd, Docklands, 3008<br>Tel: (03) 9000 1234</td></tr>
    <tr><th>Registration Fee Includes:</th><td>Entrance to the conference, refreshments, lunch, reception event on the first evening.</td></tr>
    <tr><th>Dress Code:</th><td>Business attire.</td></tr>
    <tr><th>Accommodation and Travel:</th><td>Travel and accommodation are not included in the conference fees. We do not refund airfare or hotel expenses if the event is cancelled. Contact the venue for competitive prices.</td></tr>
    <tr><th>Sponsorship Opportunities:</th><td>Sponsoring the Defence Trade Controls Conference 2015 is a fantastic way of raising your company's profile within this market and creating greater awareness of your brand. Join us to promote new and existing products and service offerings in a high-profile way amongst a select group of other sponsors and exhibitors. Contact us at <a>info@tradecontrolsevent.com</a> to find out more information.</td></tr>
    <tr><th>Early Bird Prices:</th><td>Early bird prices only apply to conference registrations and post conference training module registrations that have been paid in full by midnight of the date the earlybird closes.</td></tr>
    <tr><th>Cancellation and Substitution Policy:</th><td>Cancellations must be advised in writing at least 30 days prior to the event. An administration fee of $250 (inc. GST) will be incurred for all cancellations. A refund will not be given within 30 days of the event. If a registered attendee is unable to attend, a replacement attendee is welcome.</td></tr>
    <tr><th>Payment Terms:</th><td>Payment must be made prior to the event or admittance will not be permitted.</td></tr>
    <tr><th>Electronic Ticket:</th><td>You will receive an electronic ticket when you register online – tickets must be presented upon entry.</td></tr>
  </table>
  <h2 class="heading" style="top:334px">How To Register</h2>
  <div class="howto">Complete the registration form below and return it to us by:</div>
  <div class="contact">
    <div><svg width="9" height="9" viewBox="0 0 10 10" aria-hidden="true"><circle cx="5" cy="5" r="4.3" fill="none" stroke="#333" stroke-width=".8"/><ellipse cx="5" cy="5" rx="1.8" ry="4.3" fill="none" stroke="#333" stroke-width=".7"/><line x1=".7" y1="5" x2="9.3" y2="5" stroke="#333" stroke-width=".7"/></svg><span><b>Web</b>www.tradecontrolsevent.com</span></div>
    <div><svg width="11" height="9" viewBox="0 0 12 10" aria-hidden="true"><path d="M1 3.5C1 1.5 11 1.5 11 3.5v1.2H8.3V3.6H3.7v1.1H1z" fill="#333"/><path d="M3.2 5.2h5.6L10 9.3H2z" fill="#333"/></svg><span><b>Phone</b>+61 7 5550 1020</span></div>
    <div><svg width="10" height="9" viewBox="0 0 10 9" aria-hidden="true"><rect x="2.5" y=".5" width="5" height="3" fill="none" stroke="#333" stroke-width=".7"/><rect x=".5" y="3.5" width="9" height="4" fill="#333"/><rect x="2.5" y="6" width="5" height="2.5" fill="#fff" stroke="#333" stroke-width=".6"/></svg><span><b>Fax</b>+61 7 5550 1021</span></div>
  </div>
  <div class="folio r">Defence Trade Controls Annual Conference &nbsp; 5</div>
</section>

<section class="page p6">
  <div class="band flags" role="img" aria-label="Flag keyboard keys banner"></div>
  <h2 class="heading" style="top:83px">Conference Registration</h2>
  <div class="form">
    <div class="field">Attendee #1:</div><div class="field">Attendee #2:</div><div class="field">Attendee #3:</div><div class="field">Attendee #4:</div>
    <div class="field">Company:</div><div class="field">Address:</div><div class="field">Contact No.:</div><div class="field">Email:</div><div class="field">Dietary Needs:</div>
    <h4>Payment Method: (Please check)</h4>
    <div class="check"><span class="box"></span>Invoice</div>
    <div class="check"><span class="box"></span>Credit Card*</div>
    <div class="cards"><span>Card Type:</span><span class="check"><span class="box"></span>Card A</span><span class="check"><span class="box"></span>Card B</span><span class="check"><span class="box"></span>Card C</span></div>
    <div class="field">Card Name:</div><div class="field">Card Number:</div><div class="field">Expiry Date:</div><div class="field">Cardholder Email:</div>
    <div class="note">* Credit card payments incur a 2.5% surcharge, Card C incurs 3%.</div>
  </div>
  <div class="modules">
    <h4>1/2 day Training Module/s:</h4>
    <div class="mod"><span class="check" style="margin:0"><span class="box"></span>1 June 2015</span><span class="desc"><b>Module 1:</b> Trade Controls for Beginners</span></div>
    <div class="mod"><span class="check" style="margin:0"><span class="box"></span>4 June 2015</span><span class="desc"><b>Module 2:</b> Practical Management of Export Control Reform</span></div>
    <div class="mod"><span class="check" style="margin:0"><span class="box"></span><span><b>Module 3:</b> Tips and Hints for Best Practices Compliance</span></span></div>
    <div class="mod"><span class="check" style="margin:0"><span class="box"></span>5 June 2015</span><span class="desc"><b>Module 4:</b> Making the Best of Commerce Exceptions</span></div>
    <h4>Training Registration:</h4>
    <div>Please tick which module each attendee would like to register for.</div>
    <div class="att">Attendee #1:<div class="row">Module 1 <span class="box"></span> Module 2 <span class="box"></span> Module 3 <span class="box"></span> Module 4 <span class="box"></span></div></div>
    <div class="att">Attendee #2:<div class="row">Module 1 <span class="box"></span> Module 2 <span class="box"></span> Module 3 <span class="box"></span> Module 4 <span class="box"></span></div></div>
    <div class="att">Attendee #3:<div class="row">Module 1 <span class="box"></span> Module 2 <span class="box"></span> Module 3 <span class="box"></span> Module 4 <span class="box"></span></div></div>
    <div class="att">Attendee #4:<div class="row">Module 1 <span class="box"></span> Module 2 <span class="box"></span> Module 3 <span class="box"></span> Module 4 <span class="box"></span></div></div>
  </div>
  <div class="office">
    <b>OFFICE USE ONLY:</b>
    <div>Confirmation Sent:</div><div>Contact Person:</div><div>Invoice No.:</div><div>Paid:</div>
  </div>
</section>
</body>
</html>
```